Maltese Sunscreen

I need 2 labels for 2 sunscreens.
1: 50SPF Sunscreen suitable for oily and acne prone skin ( elexir from maltese plants that help with excess oil)
2: 50SPF Sunscreen suitable for normal skin made out of essential oils that help to calm down nervous system and stimulate sensation of relaxation.

Not sure if its too much writing on the label ?

Attached is the logo and picture of the bottle, beige tannish color 50ml

I wanted to include : Product of Malta on the label with maltese flag ( i guess smaller than the rest of the text)
I can only use " suitable" and "helps" as it is cosmetic and not medical.

Target Market(s)

Men and women

Industry/Entity Type

Skin care

Requirements
Must have
• Logo, descripción, Maltese flag “ product of Malta. Incorporate Maltese landscape like in the picture, use Maltese clover flower like in picture attached.
Nice to have
• I want the label to be very Maltese. Depict the landscape of the picture attached, use clover flower, use the Maltese lady logo

```html
<!DOCTYPE html>
<html lang="en">
<head>
<meta charset="utf-8">
<title>Qawra Skin Sunscreen SPF 50 Label</title>
<link rel="stylesheet" href="https://fonts.googleapis.com/css2?family=Gochi+Hand&family=Kalam:wght@700&family=Playfair+Display:wght@700&family=Montserrat:wght@300;400;600&display=swap">
<style>
  :root {
    --backdrop: #55504c;
    --label-top: #d6c7b9;
    --label-mid: #e6d8c9;
    --label-low: #dfc9b4;
    --ink: #2b2a2a;
    --logo-disc: #f3ebe3;
    --wave: #f6f1ec;
    --flag-red: #cf1f2b;
    --flag-white: #ffffff;
  }
  html, body {
    margin: 0;
    padding: 0;
    width: 1152px;
    height: 1200px;
    overflow: hidden;
    background: var(--backdrop);
  }
  .label {
    position: absolute;
    left: 266px;
    top: 40px;
    width: 620px;
    height: 1120px;
    background: linear-gradient(170deg, var(--label-top) 0%, var(--label-mid) 50%, var(--label-low) 100%);
    border-radius: 6px;
    overflow: hidden;
    text-align: center;
    color: var(--ink);
  }
  .sun-mark {
    position: absolute;
    left: 50%;
    top: 150px;
    width: 210px;
    height: 210px;
    margin-left: -105px;
    border-radius: 50%;
    background: radial-gradient(circle, rgba(255,255,255,0.55) 0%, rgba(255,255,255,0.15) 60%, rgba(255,255,255,0) 72%);
  }
  .brand {
    position: absolute;
    left: 50%;
    top: 207px;
    width: 104px;
    height: 104px;
    margin-left: -52px;
    border-radius: 50%;
    background: var(--logo-disc);
    display: flex;
    align-items: center;
    justify-content: center;
    font-family: "Kalam", cursive;
    font-weight: 700;
    font-size: 17px;
    line-height: 1.05;
    color: var(--ink);
  }
  .product-name {
    position: absolute;
    top: 420px;
    left: 0;
    right: 0;
    margin: 0;
    font-family: "Gochi Hand", cursive;
    font-size: 80px;
    font-weight: 400;
    line-height: 1;
    letter-spacing: -2px;
    -webkit-text-stroke: 1.4px var(--ink);
  }
  .skin-type {
    position: absolute;
    top: 510px;
    left: 0;
    right: 0;
    margin: 0;
    font-family: "Kalam", cursive;
    font-weight: 700;
    font-size: 17px;
    line-height: 1.2;
  }
  .claim {
    position: absolute;
    top: 566px;
    left: 50%;
    width: 330px;
    margin-left: -165px;
  }
  .claim svg { display: block; }
  .claim-text {
    font-family: "Montserrat", sans-serif;
    font-weight: 600;
    font-size: 7.5px;
    letter-spacing: 1px;
    padding: 6px 0;
    white-space: nowrap;
  }
  .spf-value {
    position: absolute;
    top: 610px;
    left: 0;
    right: 0;
    margin: 0;
    font-family: "Playfair Display", serif;
    font-weight: 700;
    font-size: 215px;
    line-height: 1;
  }
  .spf-unit {
    position: absolute;
    top: 835px;
    left: 0;
    right: 0;
    margin: 0;
    font-family: "Montserrat", sans-serif;
    font-weight: 300;
    font-size: 96px;
    line-height: 1;
  }
  .origin {
    position: absolute;
    top: 966px;
    left: 0;
    right: 0;
    margin: 0;
    font-family: "Kalam", cursive;
    font-weight: 700;
    font-size: 20px;
    line-height: 1.3;
  }
  .flag {
    position: absolute;
    top: 1004px;
    left: 50%;
    margin-left: -12px;
  }
  .volume {
    position: absolute;
    top: 1038px;
    left: 0;
    right: 0;
    margin: 0;
    font-family: "Montserrat", sans-serif;
    font-weight: 400;
    font-size: 17px;
    line-height: 1.2;
  }
  .wave {
    position: absolute;
    left: 0;
    bottom: 0;
    display: block;
  }
</style>
</head>
<body>
  <main class="label">
    <div class="sun-mark" role="img" aria-label="Hand-drawn sun rays surrounding the brand mark"></div>
    <div class="brand">Qawra<br>Skin</div>

    <h1 class="product-name">SUNSCREEN</h1>
    <p class="skin-type">Suitable For Oily And<br>Acne Prone Skin</p>

    <div class="claim">
      <svg width="330" height="7" viewBox="0 0 330 7" aria-hidden="true">
        <line x1="0" y1="3.5" x2="330" y2="3.5" stroke="var(--ink)" stroke-width="1"/>
        <rect x="162" y="0.5" width="6" height="6" transform="rotate(45 165 3.5)" fill="var(--ink)"/>
      </svg>
      <div class="claim-text">Elexir From Maltese Plants That Help With Excess Oil</div>
      <svg width="330" height="7" viewBox="0 0 330 7" aria-hidden="true">
        <line x1="0" y1="3.5" x2="330" y2="3.5" stroke="var(--ink)" stroke-width="1"/>
        <rect x="162" y="0.5" width="6" height="6" transform="rotate(45 165 3.5)" fill="var(--ink)"/>
      </svg>
    </div>

    <p class="spf-value">50</p>
    <p class="spf-unit">SPF</p>

    <p class="origin">Product of Malta</p>
    <svg class="flag" width="24" height="24" viewBox="0 0 24 24" role="img" aria-label="Flag of Malta">
      <clipPath id="flag-disc"><circle cx="12" cy="12" r="12"/></clipPath>
      <g clip-path="url(#flag-disc)">
        <rect x="0" y="0" width="12" height="24" fill="var(--flag-white)"/>
        <rect x="12" y="0" width="12" height="24" fill="var(--flag-red)"/>
      </g>
    </svg>
    <p class="volume">50ml</p>

    <svg class="wave" width="620" height="44" viewBox="0 0 620 44" aria-hidden="true">
      <path d="M0 26 C 140 6, 300 0, 620 16 L620 44 L0 44 Z" fill="var(--wave)" opacity="0.85"/>
    </svg>
  </main>
</body>
</html>
```